Thank You For Shopping / Hair Care Tips

I need “Thank You For Shopping”
Post cards made for my hair business !
I added pictures of post cards that I really like . I also added my LuzeKora Wigs logo for you guys to use

I want the backside of the flyer to have hair care tips !
I want people to have full directions on how to care for their wigs

Target Market(s)

Im marking to young woman to older middle aged woman
Ages 23-66 . I want my flyer to look mature And classy

Industry/Entity Type

Hair And Beauty

Font styles to use
Serif
Script

Colors
e34699
e34298
e34398

Requirements
Must have
• The flyer must have the Instagram logo with my Instagram name next to it @luze.kora.wigs__
• Also it must have my “Luze Kora Wigs” logo that I’ve uploaded in the pictures section .
• Flyer had to be two sides . One side “ thank you for shopping “ side two “hair care tips”
• My website must be on the flyer - www.luzekorawigs.example
• The flyer must match the colors of my logo
• All white . With the pink and glitter sliver you see on my logo
Nice to have
• Nice to have a glitter border
Should not have
• The flyer should not have different colors that don’t match my logo
• It shouldn’t be made without having my Instagram or website on the flyer

```html
<!DOCTYPE html>
<html lang="en">
<head>
<meta charset="utf-8">
<title>Luze Kora Wigs – Thank You Postcard</title>
<link rel="stylesheet" href="https://fonts.googleapis.com/css2?family=Great+Vibes&family=Montserrat:wght@600;700&family=Lato:wght@400;700&display=swap">
<style>
  :root{
    --pink:#e34699;
    --pink-deep:#e34298;
    --silver-dark:#8d8d8d;
    --silver-light:#d9d9d9;
    --card:#f6f7f9;
    --ink:#3c3c3c;
    --backdrop:#e34398;
  }
  *{margin:0;padding:0;box-sizing:border-box}
  html,body{width:977px;height:1200px;overflow:hidden;background:var(--backdrop)}
  .stage{position:relative;width:977px;height:1200px}
  .card{
    position:absolute;left:62px;width:854px;height:570px;overflow:hidden;
    background:radial-gradient(ellipse at 50% 20%,#ffffff 0%,var(--card) 60%,#eceef2 100%);
    box-shadow:0 4px 10px rgba(0,0,0,.25);
  }
  .card--front{top:20px}
  .card--back{top:610px}
  .glitter-frame{
    position:absolute;left:26px;top:26px;width:802px;height:518px;
    border:6px solid var(--silver-dark);
    outline:2px solid var(--silver-light);outline-offset:-4px;
  }
  .script{font-family:"Great Vibes",cursive;color:var(--pink);font-weight:400;position:absolute;white-space:nowrap}
  .thanks-title{left:40px;width:774px;text-align:center;top:52px;font-size:162px;line-height:1}
  .ribbon{position:absolute}
  .ribbon-text{
    position:absolute;left:0;width:100%;text-align:center;color:#fff;
    font-family:"Montserrat",sans-serif;font-weight:600;white-space:nowrap;
  }
  .brand-name{
    position:absolute;font-family:"Montserrat",sans-serif;font-weight:700;
    color:var(--pink);line-height:1.1;
  }
  .front-brand{left:72px;top:420px;width:200px;font-size:34px}
  .connect-heading{
    position:absolute;left:328px;top:395px;width:468px;display:flex;align-items:center;gap:12px;
    font-family:"Montserrat",sans-serif;font-weight:700;font-size:22px;color:var(--pink);letter-spacing:2px;white-space:nowrap;
  }
  .connect-heading .rule{flex:1;height:2px;background:var(--pink)}
  .contact{position:absolute;display:flex;align-items:center;gap:14px;
    font-family:"Montserrat",sans-serif;font-weight:600;color:var(--ink);letter-spacing:1.5px;white-space:nowrap}
  .contact .dot{width:26px;height:26px;border-radius:50%;background:var(--pink);flex:none}
  .front-insta{left:388px;top:444px;font-size:21px}
  .front-web{left:388px;top:491px;font-size:21px}
  .tips-title{left:68px;top:44px;font-size:76px;line-height:1.2}
  .back-brand{left:606px;top:70px;width:200px;font-size:34px;text-align:center}
  .tips{position:absolute;left:60px;list-style:none;font-family:"Lato",sans-serif;font-size:18.5px;color:var(--ink);line-height:21.6px}
  .tips li{position:relative;padding-left:13px}
  .tips li::before{content:"";position:absolute;left:0;top:8px;width:7px;height:7px;border-radius:50%;background:var(--pink)}
  .tips--wash{top:146px;width:766px}
  .tips--wash li:first-child{width:515px;margin-bottom:4px}
  .tips--bed{top:420px;width:766px}
  .pill{
    position:absolute;left:70px;top:376px;padding:4px 18px;border-radius:16px;background:var(--pink);
    color:#fff;font-family:"Montserrat",sans-serif;font-weight:700;font-size:20px;letter-spacing:1.5px;
  }
  .back-insta{left:0;top:0;height:100%;padding-left:44px;font-size:16px;color:#fff;gap:10px}
  .back-insta .dot{background:#fff;width:18px;height:18px}
  .back-web{right:52px;top:500px;font-size:15px;letter-spacing:1px;color:var(--pink);gap:10px}
  .back-web .dot{width:20px;height:20px}
</style>
</head>
<body>
<main class="stage">

  <section class="card card--front" aria-label="Thank you side">
    <div class="glitter-frame" role="img" aria-label="Silver glitter border"></div>
    <h1 class="script thanks-title">Thank You</h1>
    <div class="ribbon" style="left:58px;top:276px;width:736px;height:92px">
      <svg width="736" height="92" viewBox="0 0 736 92" aria-hidden="true">
        <polygon points="0,0 736,0 706,46 736,92 0,92 30,46" fill="var(--silver-dark)"/>
        <polygon points="12,12 724,12 700,46 724,80 12,80 36,46" fill="var(--pink)"/>
      </svg>
      <span class="ribbon-text" style="top:18px;font-size:52px;letter-spacing:8px;line-height:56px">FOR SHOPPING</span>
    </div>
    <div class="brand-name front-brand">Luze Kora Wigs</div>
    <div class="connect-heading"><span class="rule"></span>CONNECT WITH US<span class="rule"></span></div>
    <div class="contact front-insta"><span class="dot"></span>@luze.kora.wigs__</div>
    <div class="contact front-web"><span class="dot"></span>www.luzekorawigs.example</div>
  </section>

  <section class="card card--back" aria-label="Hair care tips side">
    <div class="glitter-frame" role="img" aria-label="Silver glitter border"></div>
    <h2 class="script tips-title">Hair Care Tips</h2>
    <div class="brand-name back-brand">Luze Kora Wigs</div>
    <div class="ribbon" style="left:560px;top:200px;width:264px;height:40px">
      <svg width="264" height="40" viewBox="0 0 264 40" aria-hidden="true">
        <polygon points="0,0 264,0 264,40 0,40 14,20" fill="var(--silver-dark)"/>
        <polygon points="12,5 264,5 264,35 12,35 24,20" fill="var(--pink)"/>
      </svg>
      <div class="contact back-insta"><span class="dot"></span>@luze.kora.wigs__</div>
    </div>
    <ul class="tips tips--wash">
      <li>Apply a moisture conditioner and comb hair, starting with the ends working your way up to your scalp.</li>
      <li>Leave Conditioner in for at least 15 minutes or more.</li>
      <li>Do not massage the hair.</li>
      <li>Rinse thoroughly.</li>
      <li>Scrunch hair gently to enhance the cuts.(For wave/curly patterns).</li>
      <li>When Damp, apply a dime size of anti-frizz alcohol free hair serum.</li>
      <li>Let air-dry.</li>
      <li>Do not use oil products or excessive products on curly hair, it will cause matting.</li>
      <li>Do not brush or comb hair when dry, it will cause hair to frizz and may cause hair to tangle.</li>
    </ul>
    <div class="pill">BED TIME CARE</div>
    <ul class="tips tips--bed">
      <li>Before going to bed, braid ypur hair into one loose large braid and wear a sacrf or bonnet.</li>
      <li>After waking up, undo braid and comb using a wide tooth comb(or paddle brush/through begining at the ends and working your way up to roots.</li>
      <li>Stlyle as needed</li>
    </ul>
    <div class="contact back-web"><span class="dot"></span>www.luzekorawigs.example</div>
  </section>

</main>
</body>
</html>
```